Korvane Sky Works, LLC - Business Card

I currently have a drone business that specializes in aerial photography, thermal image inspections, deer recovery, search and rescue, custom agricultural applications. i will attach my current business card as well as some logos to incorporate for a new up to date business card
Updates

Designs look the same

Sick

Target Market(s)

farmers, hunters

Contact Information for Business Card

name address phone number (as existing card i attached)

Requirements
Must have
• im good with existing business card, but would like an agricultural twist

```html
<!DOCTYPE html>
<html lang="en">
<head>
<meta charset="utf-8">
<title>Korvane Sky Works, LLC – Business Card</title>
<link rel="stylesheet" href="https://fonts.googleapis.com/css2?family=Oswald:wght@500;600&family=Montserrat:wght@600&family=Lato:wght@400&display=swap">
<style>
  :root {
    --stage-light: #b4b4b4;
    --stage-dark: #7c7c7c;
    --card-light: #e4e4e4;
    --card-dark-top: #2b2b2b;
    --card-dark-bottom: #0b0b0b;
    --brand-red: #e2222a;
    --band-red: #8f1418;
    --ink: #111111;
    --paper: #ffffff;
    --muted: #e8e8e8;
  }
  * { margin: 0; padding: 0; box-sizing: border-box; }
  html, body { width: 1200px; height: 1000px; overflow: hidden; }
  body {
    position: relative;
    background: radial-gradient(ellipse at center, var(--stage-light) 0%, var(--stage-dark) 100%);
  }
  .card {
    position: absolute;
    left: 203px;
    width: 794px;
    height: 454px;
    border-radius: 16px;
    overflow: hidden;
  }
  .card--front { top: 36px; background: var(--card-light); }
  .card--back {
    top: 510px;
    background: radial-gradient(ellipse at 55% 40%, var(--card-dark-top) 0%, var(--card-dark-bottom) 100%);
  }

  /* Service pills */
  .service {
    position: absolute;
    height: 44px;
    display: flex;
    align-items: center;
    gap: 6px;
    padding: 0 12px 0 4px;
    background: var(--paper);
    border-radius: 22px;
    box-shadow: 0 2px 4px rgba(0,0,0,0.22);
    font-family: "Oswald", sans-serif;
    font-weight: 500;
    font-size: 18px;
    color: var(--ink);
    white-space: nowrap;
  }
  .service__dot {
    width: 36px; height: 36px;
    border-radius: 50%;
    border: 3px solid var(--brand-red);
    flex: none;
  }

  /* Brand lockup */
  .brand {
    position: absolute;
    text-align: center;
    font-family: "Oswald", sans-serif;
    font-weight: 600;
    line-height: 1;
  }
  .brand__mark {
    display: block;
    margin: 0 auto 18px;
    border-radius: 50%;
    border: 5px solid var(--brand-red);
  }
  .brand__name { display: block; letter-spacing: 2px; }
  .brand__tag { display: block; letter-spacing: 5px; margin-top: 8px; }

  .brand--front { left: 0; width: 794px; top: 150px; color: var(--brand-red); }
  .brand--front .brand__mark { width: 70px; height: 70px; }
  .brand--front .brand__name { font-size: 62px; }
  .brand--front .brand__tag { font-size: 24px; }

  .brand--back { left: 30px; width: 380px; top: 148px; color: var(--brand-red); }
  .brand--back .brand__mark { width: 64px; height: 64px; }
  .brand--back .brand__name { font-size: 54px; }
  .brand--back .brand__tag { font-size: 21px; }

  /* Contact block */
  .contact { position: absolute; left: 459px; top: 94px; color: var(--paper); }
  .contact__name {
    font-family: "Montserrat", sans-serif;
    font-weight: 600;
    font-size: 32px;
    color: var(--brand-red);
    letter-spacing: 0.5px;
  }
  .contact__role {
    font-family: "Lato", sans-serif;
    font-size: 21px;
    letter-spacing: 1px;
    color: var(--muted);
    margin-top: 4px;
  }
  .contact__list { list-style: none; margin-top: 56px; font-family: "Lato", sans-serif; font-size: 21px; letter-spacing: 0.5px; }
  .contact__item { display: flex; align-items: flex-start; gap: 8px; line-height: 29px; }
  .contact__icon { width: 16px; height: 16px; margin-top: 7px; flex: none; fill: var(--brand-red); }

  .card__band {
    position: absolute;
    left: 0; right: 0; bottom: 0;
    height: 13px;
    background: var(--band-red);
  }
</style>
</head>
<body>

  <section class="card card--front" aria-label="Card front">
    <div class="service" style="left:154px; top:30px;"><span class="service__dot"></span>Aerial Photography</div>
    <div class="service" style="left:377px; top:30px;"><span class="service__dot"></span>Thermal Image Inspections</div>

    <div class="brand brand--front">
      <span class="brand__mark"></span>
      <span class="brand__name">KORVANE</span>
      <span class="brand__tag">SKY WORKS</span>
    </div>

    <div class="service" style="left:42px; top:373px;"><span class="service__dot"></span>Deer Recovery</div>
    <div class="service" style="left:227px; top:373px;"><span class="service__dot"></span>Search &amp; Rescue</div>
    <div class="service" style="left:429px; top:373px;"><span class="service__dot"></span>Custom Agricultural Applications</div>
  </section>

  <section class="card card--back" aria-label="Card back">
    <div class="brand brand--back">
      <span class="brand__mark"></span>
      <span class="brand__name">KORVANE</span>
      <span class="brand__tag">SKY WORKS</span>
    </div>

    <div class="contact">
      <p class="contact__name">DORIAN VELSK</p>
      <p class="contact__role">OWNER</p>
      <ul class="contact__list">
        <li class="contact__item">
          <svg class="contact__icon" viewBox="0 0 24 24" aria-hidden="true"><path d="M6.6 10.8a15.1 15.1 0 0 0 6.6 6.6l2.2-2.2c.3-.3.7-.4 1-.2 1.1.4 2.3.6 3.6.6.6 0 1 .4 1 1V20c0 .6-.4 1-1 1A17 17 0 0 1 3 4c0-.6.4-1 1-1h3.5c.6 0 1 .4 1 1 0 1.3.2 2.5.6 3.6.1.3 0 .7-.2 1z"/></svg>
          <span>419-555-0142</span>
        </li>
        <li class="contact__item">
          <svg class="contact__icon" viewBox="0 0 24 24" aria-hidden="true"><path d="M2 11 22 2l-9 20-2-8z"/></svg>
          <span>korvanesky@mail.com</span>
        </li>
        <li class="contact__item">
          <svg class="contact__icon" viewBox="0 0 24 24" aria-hidden="true"><path d="M12 2a10 10 0 1 0 0 20 10 10 0 0 0 0-20zm6.9 6h-3a15.6 15.6 0 0 0-1.4-3.6A8 8 0 0 1 18.9 8zM12 4c.8 1.2 1.5 2.5 1.9 4h-3.8c.4-1.5 1.1-2.8 1.9-4zM4.3 14a8 8 0 0 1 0-4h3.4a16 16 0 0 0 0 4zm.8 2h3a15.6 15.6 0 0 0 1.4 3.6A8 8 0 0 1 5.1 16zm3-8h-3a8 8 0 0 1 4.3-3.6C8.9 5.6 8.4 6.8 8.1 8zM12 20c-.8-1.2-1.5-2.5-1.9-4h3.8c-.4 1.5-1.1 2.8-1.9 4zm2.3-6H9.7a14 14 0 0 1 0-4h4.6a14 14 0 0 1 0 4zm.3 5.6c.6-1.1 1.1-2.3 1.4-3.6h3a8 8 0 0 1-4.4 3.6zm1.7-5.6a16 16 0 0 0 0-4h3.4a8 8 0 0 1 0 4z"/></svg>
          <span>www.korvanesky.com</span>
        </li>
        <li class="contact__item">
          <svg class="contact__icon" viewBox="0 0 24 24" aria-hidden="true"><path d="M12 2a7 7 0 0 0-7 7c0 5.2 7 13 7 13s7-7.8 7-13a7 7 0 0 0-7-7zm0 9.5A2.5 2.5 0 1 1 12 6.5a2.5 2.5 0 0 1 0 5z"/></svg>
          <span>214 N. Elm St.<br>Marlow, OH 45899</span>
        </li>
      </ul>
    </div>

    <div class="card__band"></div>
  </section>

</body>
</html>
```